Fantasy-Roman sucht eBook-Cover
Bin sehr glücklich mit dem Ergebnis! Alle Erwartungen wurden erfüllt und alle Anregungen oder Veränderungswünsche wurden professionell umgesetzt. Ich kann die Zusammenarbeit mit der Designerin nur empfehlen und werde diese auch in Zukunft anstreben.
Zielgruppe
Autorin; Zielgruppe: Jugendliche, die sich für Mystik und Fantasy interessieren; Covergestaltung eBook
Aufgabenstellung
Es handelt sich um ein Jugendbuch im Genre Fantasy. Dunkelroter Hintergrund, das Symbol sollte deutlich sichtbar sein und ein verspielt verschnörkelter Rahmen wäre schön. Mystisch

```html
<!DOCTYPE html>
<html lang="de">
<head>
<meta charset="utf-8">
<title>Der Kreis der Avena – eBook-Cover</title>
<link rel="stylesheet" href="https://fonts.googleapis.com/css2?family=Cinzel:wght@400;600&family=Cinzel+Decorative:wght@700&display=swap">
<style>
  :root {
    --page: #ffffff;
    --night: #170b08;
    --wine: #4a1712;
    --ember: #b8352c;
    --glow: #f6e9dc;
    --gold: #e9cf9a;
    --ink: #4b3e3a;
    --seal: #7a0f0f;
    --night-mono: #0c0c0c;
    --ash: #3a3a3a;
    --silver: #8a8a8a;
    --glow-mono: #e6e6e6;
    --ink-mono: #505050;
    --seal-mono: #262626;
  }
  * { margin: 0; padding: 0; box-sizing: border-box; }
  html, body { width: 1200px; height: 1200px; overflow: hidden; background: var(--page); }
  .canvas { position: relative; width: 1200px; height: 1200px; }

  .cover {
    position: absolute; top: 155px; width: 555px; height: 887px; overflow: hidden;
  }
  .cover--colour { left: 26px; }
  .cover--mono { left: 615px; }

  .cover-art { position: absolute; inset: 0; }
  .cover--colour .cover-art {
    background: radial-gradient(ellipse 70% 50% at 50% 52%, var(--glow) 0%, var(--ember) 35%, var(--wine) 65%, var(--night) 100%);
  }
  .cover--mono .cover-art {
    background: radial-gradient(ellipse 70% 50% at 50% 52%, var(--glow-mono) 0%, var(--silver) 35%, var(--ash) 65%, var(--night-mono) 100%);
  }

  .author {
    position: absolute; top: 96px; width: 100%; text-align: center;
    font-family: "Cinzel", serif; font-weight: 600; font-size: 27px; letter-spacing: 1px;
    color: var(--gold); text-shadow: 0 0 6px rgba(0,0,0,0.6);
  }
  .cover--mono .author { color: #d8d8d8; }

  .title {
    position: absolute; width: 100%; text-align: center; white-space: nowrap;
    font-family: "Cinzel Decorative", serif; font-weight: 700; font-size: 76px; line-height: 1;
    color: var(--ink);
    text-shadow: 0 0 8px #fff6ec, 0 0 18px rgba(255,245,230,0.9), 0 0 30px rgba(255,240,220,0.6);
  }
  .cover--mono .title { color: var(--ink-mono); text-shadow: 0 0 8px #fff, 0 0 18px rgba(255,255,255,0.9), 0 0 30px rgba(255,255,255,0.6); }
  .title--top { top: 318px; }
  .title--bottom { top: 515px; }

  .emblem {
    position: absolute; left: 232px; top: 412px; width: 92px; height: 90px;
    border-radius: 6px; background: var(--seal);
  }
  .cover--mono .emblem { background: var(--seal-mono); }
</style>
</head>
<body>
<main class="canvas">
  <section class="cover cover--colour">
    <div class="cover-art" role="img" aria-label="Illustration: leuchtende rote Sphäre wie eine Sonnenfinsternis mit Lichtstrahlen, umgeben von einem verschnörkelten ovalen Zierrahmen auf dunkelrotem Grund"></div>
    <p class="author">Liora Brandt</p>
    <h1 class="title title--top">DER KREIS</h1>
    <div class="emblem" role="img" aria-label="Symbol des Buches"></div>
    <h2 class="title title--bottom">DER AVENA</h2>
  </section>

  <section class="cover cover--mono">
    <div class="cover-art" role="img" aria-label="Illustration in Graustufen: leuchtende Sphäre wie eine Sonnenfinsternis mit Lichtstrahlen, umgeben von einem verschnörkelten ovalen Zierrahmen auf schwarzem Grund"></div>
    <p class="author">Liora Brandt</p>
    <h1 class="title title--top">DER KREIS</h1>
    <div class="emblem" role="img" aria-label="Symbol des Buches"></div>
    <h2 class="title title--bottom">DER AVENA</h2>
  </section>
</main>
</body>
</html>
```